Australian Trucking Company Requires Professional Looking Stationary

We require a professional looking stationary design that incorporates our newly designed logo.

Our business, called "Vell Haulage Contracting", provides contracting work, transport and logistics to business in Western Australia particularly with links to the mining sector.

We are a small business looking to expand and our new logo and our new stationary will help develop our brand image in our market place.

Target Market(s)

Businesses and Corporation with links to the Mining Sector

Industry/Entity Type

Small Business

Requirements
Must have
• The letterhead must have the following details:
The new logo

Text saying: "Vell Haulage Pty Ltd (ACN 582 306 917) ATF The Vell Discretionary Trust T/AS"
"ABN 71 840 239 568"
Address "P.O Box 817 Ashbury WA, 6912"
Phone: 08 9172 5840
Email: vellhaul@mailnest.com.au

The text on the letterhead should be editable as the details are likely to change in the near future. Provision should be made for a website address all though one isn't available at the moment.

The styling, layout and font text is entirely up to the designer.

```html
<!DOCTYPE html>
<html lang="en">
<head>
<meta charset="utf-8">
<title>Vell Haulage Contracting – Business Card</title>
<link rel="stylesheet" href="https://fonts.googleapis.com/css2?family=PT+Sans:wght@400;700&display=swap">
<style>
  :root {
    --page-bg: #e9e6e2;
    --card-white: #ffffff;
    --card-grey: #dcdcdc;
    --brand-red: #c3161f;
    --brand-red-dark: #8e0f14;
    --brand-red-bright: #e11a26;
    --swoosh-grey: #b9b9b9;
    --ink: #1e1e1e;
    --ink-soft: #2c2c2c;
    --white: #ffffff;
    --truck-dark: #2a2a2a;
    --truck-mid: #6a6a6a;
  }
  * { box-sizing: border-box; margin: 0; padding: 0; }
  html, body { width: 1200px; height: 426px; overflow: hidden; }
  body {
    background: var(--page-bg);
    font-family: "PT Sans", Arial, sans-serif;
    position: relative;
  }
  .card {
    position: absolute;
    top: 62px;
    width: 527px;
    height: 295px;
    border-radius: 18px;
    overflow: hidden;
    box-shadow: 0 4px 10px rgba(0,0,0,0.25);
  }
  .card--front {
    left: 40px;
    background: linear-gradient(180deg, var(--card-white) 0%, #f1f1f1 60%, #e8e8e8 100%);
  }
  .card--back {
    left: 590px;
    width: 520px;
    background: linear-gradient(90deg, #f7f7f7 0%, var(--card-white) 45%, var(--card-grey) 100%);
  }
  .wave { position: absolute; left: 0; top: 0; }

  .logo-truck {
    position: absolute;
    left: 38px; top: 24px;
    width: 110px; height: 90px;
    border-radius: 6px;
    background: linear-gradient(135deg, var(--truck-mid), #a9a9a9);
  }
  .brand-name {
    position: absolute;
    left: 166px; top: 30px;
    color: var(--brand-red);
    font-weight: 700;
    font-size: 31px;
    line-height: 30px;
    text-transform: uppercase;
    letter-spacing: 0.5px;
  }
  .contact {
    position: absolute;
    left: 160px; top: 146px;
    font-size: 13px;
    color: var(--ink-soft);
  }
  .contact__row { display: flex; align-items: center; gap: 4px; height: 22px; }
  .contact__row span + svg { margin-left: 12px; }
  .contact svg { width: 11px; height: 11px; fill: var(--ink); }

  .mini-truck {
    position: absolute;
    left: 422px; top: 176px;
    width: 68px; height: 58px;
    border-radius: 4px;
    background: linear-gradient(135deg, var(--truck-dark), #555);
  }
  .person {
    position: absolute;
    left: 33px; top: 220px;
    color: var(--white);
    text-align: center;
  }
  .person__name { font-size: 18px; font-weight: 700; line-height: 22px; }
  .person__role { font-size: 12px; line-height: 16px; }
  .website {
    position: absolute;
    left: 40px; top: 270px;
    color: var(--white);
    font-size: 12.5px;
  }
  .legal {
    position: absolute;
    right: 30px; top: 236px;
    color: var(--white);
    font-size: 12px;
    line-height: 17px;
    text-align: right;
  }
  .legal__abn { margin-top: 9px; }

  .back-truck {
    position: absolute;
    left: 200px; top: 28px;
    width: 275px; height: 232px;
    border-radius: 10px;
    background: linear-gradient(135deg, var(--truck-dark), #4a4a4a);
  }
</style>
</head>
<body>

<section class="card card--front" aria-label="Business card front">
  <svg class="wave" width="527" height="295" viewBox="0 0 527 295" aria-hidden="true">
    <defs>
      <linearGradient id="redFill" x1="0" y1="0" x2="1" y2="1">
        <stop offset="0" stop-color="var(--brand-red-dark)"/>
        <stop offset="0.45" stop-color="var(--brand-red-bright)"/>
        <stop offset="1" stop-color="var(--brand-red-dark)"/>
      </linearGradient>
      <linearGradient id="greyFill" x1="0" y1="0" x2="1" y2="0">
        <stop offset="0" stop-color="#d6d6d6"/>
        <stop offset="1" stop-color="var(--swoosh-grey)"/>
      </linearGradient>
    </defs>
    <path d="M0 165 C120 175 230 215 330 200 C420 186 480 150 527 128 L527 295 L0 295 Z" fill="url(#greyFill)"/>
    <path d="M0 180 C120 188 230 222 330 212 C420 202 480 176 527 160 L527 295 L0 295 Z" fill="url(#redFill)"/>
  </svg>

  <div class="logo-truck" role="img" aria-label="Logo truck illustration in grey"></div>
  <div class="brand-name">Vell<br>Haulage<br>Contracting</div>

  <div class="contact">
    <div class="contact__row">
      <svg viewBox="0 0 12 12" aria-hidden="true"><path d="M2.5 0.8 L4.5 3.4 L3.4 4.6 C4.1 6.1 5.6 7.7 7.2 8.5 L8.4 7.4 L11 9.4 L9.9 11.2 C5 10.8 1 6.6 0.8 1.9 Z"/></svg>
      <span>08 9172 5840</span>
      <svg viewBox="0 0 12 12" aria-hidden="true"><path d="M0.5 2 H11.5 V10 H0.5 Z M1.5 3 V9 H10.5 V3 L6 6.5 Z M2.2 3 L6 5.8 L9.8 3 Z" fill-rule="evenodd"/></svg>
      <span>vellhaul@mailnest.com.au</span>
    </div>
    <div class="contact__row">
      <svg viewBox="0 0 12 12" aria-hidden="true"><path d="M6 1 L11.5 6 H10 V11 H7.3 V8 H4.7 V11 H2 V6 H0.5 Z"/></svg>
      <span>P.O Box 817 Ashbury WA, 6912</span>
    </div>
  </div>

  <div class="mini-truck" role="img" aria-label="Small truck illustration"></div>

  <div class="person">
    <div class="person__name">Persons name</div>
    <div class="person__role">Manager</div>
  </div>
  <div class="website">www.vellhaulsite.com</div>

  <div class="legal">
    <div>Vell Haulage Pty Ltd (ACN 582 306 917)</div>
    <div>ATF The Vell Discretionary Trust T/AS</div>
    <div class="legal__abn">ABN 71 840 239 568</div>
  </div>
</section>

<section class="card card--back" aria-label="Business card back">
  <div class="back-truck" role="img" aria-label="Large black truck illustration"></div>
</section>

</body>
</html>
```